Business Card Design for Technology Company

New business card design needed for technology company director.
Ideally, the design will fit the style and nature of the industry. We are a supplier of quality products and services, and we hope the design will give customers and suppliers this impression.

Target Market(s)

3D Printing Industry

Industry/Entity Type

Technology Equipment

Contact Information for Business Card

Name: Marcus Lyle
Title: Director
Company address: Factory K4, 7B Morland Road, Ashmere Kelvale Australia 3290
Telephone: +61-3-8555 6413
Email: marcus.lyle@veranox.com.au
Website: www.veranox.com.au

Requirements
Must have
• All information in business card details
• Company logo
• '3D Printers and 3D Print Filaments' at proper place
Nice to have
• Style to fit the industry
• Colour to fit logo

```html
<!DOCTYPE html>
<html lang="en">
<head>
<meta charset="UTF-8">
<title>Veranox Technology — Business Card</title>
<link rel="stylesheet" href="https://fonts.googleapis.com/css2?family=Open+Sans:wght@400;600;700&display=swap">
<style>
  :root {
    --backdrop: #d9dcde;
    --brand-blue: #0b8fcc;
    --brand-teal: #8ed4d2;
    --frame-line: #e9fbfa;
    --ink: #1d1f22;
    --ink-soft: #4a4f55;
    --paper: #ffffff;
  }
  * { box-sizing: border-box; margin: 0; padding: 0; }
  html, body {
    width: 1200px; height: 834px; overflow: hidden;
    background: var(--backdrop);
    font-family: "Open Sans", Arial, sans-serif;
  }
  .canvas {
    position: relative; width: 1200px; height: 834px;
    display: flex; align-items: center; justify-content: center; gap: 50px;
  }
  .card {
    position: relative; width: 520px; height: 318px;
    box-shadow: 0 10px 28px rgba(0,0,0,.18);
    overflow: hidden;
  }

  /* Front */
  .card-front { display: flex; background: var(--paper); }
  .contact-panel {
    width: 46%; background: var(--brand-blue); color: var(--paper);
    padding: 30px 14px 0 24px; position: relative;
  }
  .holder-name { font-size: 17px; font-weight: 700; letter-spacing: .5px; text-transform: uppercase; }
  .holder-title { font-size: 9px; letter-spacing: 1px; text-transform: uppercase; opacity: .85; margin-top: 2px; }
  .contact-list { list-style: none; margin-top: 34px; font-size: 11px; line-height: 1.3; white-space: nowrap; }
  .contact-list li { display: flex; align-items: flex-start; gap: 8px; margin-bottom: 7px; }
  .contact-list svg { flex: none; width: 11px; height: 11px; margin-top: 2px; fill: var(--paper); }
  .panel-rule {
    position: absolute; left: 24px; right: 0; bottom: 58px; height: 1px;
    background: linear-gradient(to right, rgba(255,255,255,.7), rgba(255,255,255,0));
  }
  .brand-panel {
    flex: 1; position: relative;
    display: flex; flex-direction: column; align-items: center; justify-content: center;
  }
  .brand-mark { display: flex; align-items: center; gap: 12px; }
  .brand-square { width: 30px; height: 30px; background: var(--brand-blue); }
  .brand-name {
    font-size: 30px; font-weight: 700; letter-spacing: 3px; color: var(--ink);
    text-transform: uppercase; line-height: 1;
  }
  .brand-sub {
    font-size: 10px; font-weight: 700; letter-spacing: 6px; color: var(--ink);
    text-transform: uppercase; margin-top: 8px; margin-left: 42px;
  }
  .brand-panel .back-brand { margin-top: -30px; }
  .tagline {
    position: absolute; left: 0; right: 0; bottom: 24px;
    text-align: center; font-size: 11.5px; font-weight: 700; color: var(--ink-soft);
  }
  .tagline-rule {
    position: absolute; left: 0; right: 24px; bottom: 58px; height: 1px;
    background: linear-gradient(to right, var(--brand-blue), rgba(11,143,204,0));
  }

  /* Back */
  .card-back {
    background: var(--brand-teal);
    display: flex; align-items: center; justify-content: center;
  }
  .card-frame { position: absolute; inset: 0; }
  .back-brand { display: flex; flex-direction: column; align-items: center; position: relative; }
</style>
</head>
<body>
<main class="canvas">

  <section class="card card-front" aria-label="Business card front">
    <div class="contact-panel">
      <h1 class="holder-name">Marcus Lyle</h1>
      <p class="holder-title">Director</p>
      <ul class="contact-list">
        <li><svg viewBox="0 0 12 12"><path d="M3 0h6a1 1 0 0 1 1 1v10a1 1 0 0 1-1 1H3a1 1 0 0 1-1-1V1a1 1 0 0 1 1-1zm0 1.5v8h6v-8z"/></svg>+61-3-8555 6413</li>
        <li><svg viewBox="0 0 12 12"><path d="M0 2h12v8H0zm1 1v.4l5 3.2 5-3.2V3z"/></svg>marcus.lyle@veranox.com.au</li>
        <li><svg viewBox="0 0 12 12"><path d="M6 0a6 6 0 1 0 0 12A6 6 0 0 0 6 0zm0 1c.8 0 1.6 1.7 1.8 4H4.2C4.4 2.7 5.2 1 6 1zM1.1 5h2.1c.1-1.5.4-2.8.9-3.6A5 5 0 0 0 1.1 5zm7.7 0h2.1a5 5 0 0 0-3-3.6c.5.8.8 2.1.9 3.6zM1.1 7a5 5 0 0 0 3 3.6c-.5-.8-.8-2.1-.9-3.6zm3.1 0c.2 2.3 1 4 1.8 4s1.6-1.7 1.8-4zm4.6 0c-.1 1.5-.4 2.8-.9 3.6a5 5 0 0 0 3-3.6z"/></svg>www.veranox.com.au</li>
        <li><svg viewBox="0 0 12 12"><path d="M6 0a4 4 0 0 0-4 4c0 3 4 8 4 8s4-5 4-8a4 4 0 0 0-4-4zm0 5.5A1.5 1.5 0 1 1 6 2.5a1.5 1.5 0 0 1 0 3z"/></svg><span>Factory K4, 7B Morland Road<br>Ashmere Kelvale Australia 3290</span></li>
      </ul>
      <div class="panel-rule"></div>
    </div>
    <div class="brand-panel">
      <div class="back-brand">
        <div class="brand-mark">
          <span class="brand-square"></span>
          <span class="brand-name">Veranox</span>
        </div>
        <span class="brand-sub">Technology</span>
      </div>
      <div class="tagline-rule"></div>
      <p class="tagline">3D Printers and 3D Print Filaments</p>
    </div>
  </section>

  <section class="card card-back" aria-label="Business card back">
    <svg class="card-frame" viewBox="0 0 520 318" aria-hidden="true">
      <path d="M34 18 H486 A16 16 0 0 0 502 34 V284 A16 16 0 0 0 486 300 H34 A16 16 0 0 0 18 284 V34 A16 16 0 0 0 34 18 Z"
            fill="none" stroke="var(--frame-line)" stroke-width="1.2"/>
    </svg>
    <div class="back-brand">
      <div class="brand-mark">
        <span class="brand-square"></span>
        <span class="brand-name">Veranox</span>
      </div>
      <span class="brand-sub">Technology</span>
    </div>
  </section>

</main>
</body>
</html>
```